business card for law firm that reflects the web site -www.MarlaQuentby.com. That is pleasant to read

We need a business card for a small law firm. Your company designed our logo - tree of life - which I can provide to the designers. The card should be on both sides. Use the coloring from the web site (www.MarlaQuentby.com) and logo (I have several formats). I am attaching the logo, but not sure what format to use.

First side name of firm: Law Office of M.K. Quentby, P.A. 4819 West Pallisor, Suite 300, Phoenix, AZ 85016, Phone: 602.555.3841, Fax: 602.555.7290, web site: www.MarlaQuentby.com, email: MQuentby@MarlaQuentby.com.
Marla K. Quentby Bankruptcy and Foreclosure Attorney & Counselor.
Back side (perhaps vertical) the logo and then Notes with lines. At the bottom: Proud to help people and small businesses file for bankruptcy protection. We are a debt relief agency.
Updates

I have several versions of the logo. Will be happy to share whatever you need. Added Sunday, April 3, 2016

Target Market(s)

everyone

Industry/Entity Type

Legal

Contact Information for Business Card

I prefer something unique (rounded edges, design that adopts my web site - www.MarlaQuentby.com.

Font styles to use
Serif

Requirements
Must have
• First side name of firm: Law Office of M.K. Quentby, P.A. 4819 West Pallisor, Suite 300, Phoenix, AZ 85016, Phone: 602.555.3841, Fax: 602.555.7290, web site: www.MarlaQuentby.com, email: MQuentby@MarlaQuentby.com.
• Marla K. Quentby Bankruptcy and Foreclosure Attorney & Counselor.
• Back side (perhaps vertical) the logo and then Notes with lines. At the bottom: Proud to help people and small businesses file for bankruptcy protection. We are a debt relief agency.
• Green and brown colors that reflect the web site: www.MarlaQuentby.com
Should not have
• Type so small that older people cannot read.

```html
<!DOCTYPE html>
<html lang="en">
<head>
<meta charset="utf-8">
<title>Law Office of M.K. Quentby, P.A. — Business Card</title>
<link rel="stylesheet" href="https://fonts.googleapis.com/css2?family=Jost:wght@400;500&family=Libre+Baskerville:wght@400&display=swap">
<style>
  :root {
    --brown: #4a2a1a;
    --brown-deep: #3d2215;
    --green: #1f4a2c;
    --green-text: #2b5a34;
    --beige: #dcd7c1;
    --cream: #ece6cf;
    --paper: #f4f4f2;
    --rule: #b9b9b9;
    --ink: #3a2418;
    --bg: #e9e6e0;
  }
  * { box-sizing: border-box; margin: 0; padding: 0; }
  html, body { width: 1200px; height: 1200px; overflow: hidden; }
  body { background: var(--bg); position: relative; font-family: "Jost", sans-serif; }

  .card { position: absolute; overflow: hidden; border-radius: 10px; box-shadow: 0 6px 18px rgba(0,0,0,.18); background: var(--paper); }

  /* Front */
  .card--front { left: 50px; top: 405px; width: 680px; height: 389px; }
  .front__strip { position: absolute; left: 0; top: 0; width: 48px; height: 100%; background: var(--brown); }
  .stitch-v { position: absolute; top: 10px; bottom: 10px; border-left: 1.5px dashed var(--cream); }
  .front__strip .stitch-v { left: 34px; }
  .front__panel { position: absolute; left: 48px; top: 0; width: 212px; height: 100%; background: var(--beige); text-align: center; }
  .seal { display: flex; align-items: center; justify-content: center; border-radius: 50%; background: var(--brown-deep); }
  .seal__name { font-family: "Libre Baskerville", serif; color: var(--cream); font-size: 17px; }
  .front__panel .seal { width: 150px; height: 150px; margin: 26px auto 0; }
  .firm { font-family: "Libre Baskerville", serif; color: var(--green-text); }
  .firm__pre { font-size: 12px; letter-spacing: .5px; display: block; }
  .firm__name { font-size: 17px; display: block; }
  .front__panel .firm { margin-top: 16px; line-height: 1.25; }
  .tagline { margin-top: 26px; font-size: 12.5px; color: var(--ink); line-height: 1.5; }

  .front__info { position: absolute; left: 290px; top: 58px; color: var(--ink); }
  .person { font-size: 25px; font-weight: 500; letter-spacing: .3px; }
  .role { margin-top: 6px; font-size: 14px; color: var(--green-text); line-height: 1.3; }
  .address { margin-top: 20px; font-size: 15px; line-height: 1.35; font-style: normal; }
  .contacts { margin-top: 18px; list-style: none; font-size: 15px; line-height: 1.45; }
  .contacts li { display: flex; align-items: center; gap: 10px; }
  .contacts svg { width: 13px; height: 13px; fill: var(--green); flex: none; }

  /* Back */
  .card--back { left: 770px; top: 260px; width: 389px; height: 680px; }
  .back__head { position: absolute; left: 0; top: 0; width: 100%; height: 285px; background: var(--brown); text-align: center; }
  .stitch-h { position: absolute; left: 10px; right: 10px; border-top: 1.5px dashed var(--cream); }
  .back__head .stitch-h { bottom: 14px; }
  .back__head .seal { width: 160px; height: 160px; margin: 26px auto 0; background: var(--green); border: 3px solid var(--cream); }
  .back__head .firm { color: var(--cream); margin-top: 14px; line-height: 1.25; }
  .notes { position: absolute; left: 0; top: 285px; width: 100%; height: 250px; padding: 36px 30px 0; }
  .notes__line { height: 1px; background: var(--rule); margin-bottom: 30px; }
  .back__foot { position: absolute; left: 0; bottom: 0; width: 100%; height: 145px; background: var(--green); color: #eef0e8; display: flex; align-items: center; justify-content: center; text-align: center; font-size: 15px; line-height: 1.45; padding: 0 26px; }
</style>
</head>
<body>

<section class="card card--front" aria-label="Card front">
  <div class="front__strip"><span class="stitch-v"></span></div>
  <div class="front__panel">
    <div class="seal"><span class="seal__name">Quentby</span></div>
    <p class="firm"><span class="firm__pre">LAW OFFICE OF</span><span class="firm__name">M.K. QUENTBY, P.A.</span></p>
    <p class="tagline">Helping You<br>Get Your Life Back On Track</p>
  </div>
  <div class="front__info">
    <h1 class="person">Marla K. Quentby</h1>
    <p class="role">Bankruptcy and Foreclosure<br>Attorney &amp; Counselor.</p>
    <address class="address">4819 West Pallisor, Suite 300<br>Phoenix, AZ 85016</address>
    <ul class="contacts">
      <li><svg viewBox="0 0 16 16"><path d="M3 1h3l1 4-2 1a9 9 0 0 0 5 5l1-2 4 1v3a2 2 0 0 1-2 2C7 15 1 9 1 3a2 2 0 0 1 2-2z"/></svg>602.555.3841</li>
      <li><svg viewBox="0 0 16 16"><path d="M4 1h7v4H4zM1 6h14v7h-3v2H4v-2H1zm4 5v3h6v-3z"/></svg>602.555.7290</li>
      <li><svg viewBox="0 0 16 16"><path d="M1 3h14v10H1zm1.5 1.5L8 9l5.5-4.5z" fill-rule="evenodd"/></svg>MQuentby@MarlaQuentby.com</li>
      <li><svg viewBox="0 0 16 16"><circle cx="8" cy="8" r="7"/></svg>www.MarlaQuentby.com</li>
    </ul>
  </div>
</section>

<section class="card card--back" aria-label="Card back">
  <div class="back__head">
    <div class="seal"><span class="seal__name">Quentby</span></div>
    <p class="firm"><span class="firm__pre">LAW OFFICE OF</span><span class="firm__name">M.K. QUENTBY, P.A.</span></p>
    <span class="stitch-h"></span>
  </div>
  <div class="notes" aria-label="Lines for notes">
    <div class="notes__line"></div><div class="notes__line"></div><div class="notes__line"></div>
    <div class="notes__line"></div><div class="notes__line"></div><div class="notes__line"></div>
    <div class="notes__line"></div>
  </div>
  <p class="back__foot">Proud to help people and small businesses file for bankruptcy protection. We are a debt relief agency.</p>
</section>

</body>
</html>
```